Exciting new aperitif brand needs a great label

Vel-Orin is a wonderful rich new premium-priced bitter aperitif, with a deep red colour, from a 100+ year old distillery (1890) near Turin in the Piedmont region of Italy. Inspired by Torvesi, it is perfectly formulated to elevate the classic Baldetti cocktail (and variations on it). It also goes perfectly in a Spritz or a long mixed drink with soda or tonic. The name Vel-Orin is derived from the French for 'peak' and the Italian word for 'love'.

The label, which should take inspiration from Torvesi, but be distinctively different, can incoporate any number of premium label embellishments (foil, embossing, textures etc) and should be no greater than 11cm (height) x 9cm (width) with any core imagery restricted to a width of c.7cm.

The attached mood board should act as inspiration and colour should largely be restricted to reds, blues, whites and perhaps orange. For completeness, the label should note that the ABV is 25% and the bottle size 70cl.

Target Market(s)

21-45yr olds - equal split female/male

Colors
0054AA
0677BA
7BADD7
CADEEF
E8F1F8
0094D4
00A9DD
6FCCEA
C7EBF8
E9F6FB
EE7325
F08F49
F5BC92
FAE3D3
FDF4ED
EB3D1F
EC4F4E
F09395
F8D3D4
FCEDEE

Requirements
Must have
• Great lettering design on the name Vel-Orin

```html
<!DOCTYPE html>
<html lang="en">
<head>
<meta charset="utf-8">
<title>Vel-Orin Bitter Label</title>
<link rel="stylesheet" href="https://fonts.googleapis.com/css2?family=Playfair+Display:wght@400;700;900&family=Teko:wght@600&display=swap">
<style>
  :root {
    --backdrop: #450d12;
    --label-edge: #e9f6fb;
    --panel-light: #f6fbfe;
    --panel-blue: #d6ecf8;
    --gold-light: #f3d98a;
    --gold: #c9a45a;
    --gold-dark: #8f6c32;
    --banner-blue: #1257aa;
    --banner-ring: #0677ba;
    --name-white: #ffffff;
    --accent-red: #eb3d1f;
    --ink: #1c1c24;
  }
  html, body {
    margin: 0;
    padding: 0;
    width: 1199px;
    height: 1200px;
    overflow: hidden;
    background: var(--backdrop);
  }
  .label-art {
    display: block;
    width: 1199px;
    height: 1200px;
  }
  .label-text {
    font-family: "Playfair Display", Georgia, serif;
    font-variant-numeric: lining-nums;
    text-anchor: middle;
  }
  .display-text {
    font-family: "Teko", "Arial Narrow", sans-serif;
    font-weight: 600;
    text-anchor: middle;
  }
  .heritage { fill: var(--ink); font-weight: 700; letter-spacing: 4px; }
  .brand-name { fill: var(--name-white); }
  .serve-line { fill: var(--accent-red); font-weight: 700; }
  .strength { fill: var(--ink); font-weight: 700; }
  .volume { fill: var(--ink); font-weight: 700; text-anchor: end; }
  .style-badge-text { fill: var(--name-white); letter-spacing: 2px; }
</style>
</head>
<body>
<svg class="label-art" viewBox="-90 340 1400 1400" xmlns="http://www.w3.org/2000/svg">
  <defs>
    <linearGradient id="goldFoil" x1="0" y1="0" x2="1" y2="1">
      <stop offset="0" stop-color="var(--gold-dark)"/>
      <stop offset="0.3" stop-color="var(--gold-light)"/>
      <stop offset="0.55" stop-color="var(--gold)"/>
      <stop offset="0.8" stop-color="var(--gold-light)"/>
      <stop offset="1" stop-color="var(--gold-dark)"/>
    </linearGradient>
    <linearGradient id="goldRule" x1="0" y1="0" x2="1" y2="0">
      <stop offset="0" stop-color="var(--gold-dark)"/>
      <stop offset="0.5" stop-color="var(--gold-light)"/>
      <stop offset="1" stop-color="var(--gold-dark)"/>
    </linearGradient>
    <radialGradient id="panelGlow" cx="0.5" cy="0.45" r="0.7">
      <stop offset="0" stop-color="var(--panel-light)"/>
      <stop offset="1" stop-color="var(--panel-blue)"/>
    </radialGradient>
    <linearGradient id="flourishTone" x1="0" y1="0" x2="1" y2="0">
      <stop offset="0" stop-color="var(--gold)" stop-opacity="0"/>
      <stop offset="0.5" stop-color="var(--gold)" stop-opacity="0.35"/>
      <stop offset="1" stop-color="var(--gold)" stop-opacity="0"/>
    </linearGradient>
    <path id="serveArc" d="M318,1300 Q610,1178 902,1300"/>
  </defs>

  <!-- label body -->
  <path class="label-edge" d="M310,415 H910 Q910,478 960,478 V1570 Q910,1570 910,1630 H310 Q310,1570 262,1570 V478 Q310,478 310,415 Z" fill="var(--label-edge)" stroke="url(#goldFoil)" stroke-width="5"/>
  <path class="label-frame" d="M330,440 H890 Q890,498 935,498 V1550 Q890,1550 890,1605 H330 Q330,1550 287,1550 V498 Q330,498 330,440 Z" fill="url(#goldFoil)"/>
  <path class="label-panel" d="M352,472 H868 L910,515 V1525 L868,1568 H352 L310,1525 V515 Z" fill="url(#panelGlow)" stroke="var(--label-edge)" stroke-width="4"/>

  <!-- top rule -->
  <g class="top-rule">
    <rect x="425" y="527" width="365" height="6" rx="3" fill="url(#goldRule)"/>
    <circle cx="420" cy="530" r="8" fill="none" stroke="var(--gold)" stroke-width="4"/>
    <circle cx="795" cy="530" r="8" fill="none" stroke="var(--gold)" stroke-width="4"/>
  </g>

  <text class="label-text heritage" x="610" y="584"><tspan font-size="40">100+</tspan><tspan font-size="28" dx="10">YEAR</tspan></text>
  <text class="label-text heritage" x="612" y="634"><tspan font-size="27">OLD DISTILLERY</tspan><tspan font-size="38" dx="10">(1890)</tspan></text>

  <!-- name banner -->
  <path class="name-banner" d="M200,680 H1020 Q1058,680 1058,718 V1050 Q1058,1092 1018,1077 Q610,930 202,1077 Q162,1092 162,1050 V718 Q162,680 200,680 Z" fill="var(--banner-blue)" stroke="url(#goldFoil)" stroke-width="9"/>
  <path class="name-banner-ring" d="M205,700 H1015 Q1038,700 1038,722 V1040 Q1038,1062 1015,1054 Q610,912 205,1054 Q182,1062 182,1040 V722 Q182,700 205,700 Z" fill="none" stroke="var(--banner-ring)" stroke-width="6"/>
  <text class="display-text brand-name" x="610" y="1000" font-size="370" textLength="800" lengthAdjust="spacingAndGlyphs">VEL-ORIN</text>

  <!-- serve suggestion -->
  <text class="label-text serve-line" x="606" y="1192" font-size="58">CLASSIC</text>
  <text class="label-text serve-line" font-size="52"><textPath href="#serveArc" startOffset="50%" text-anchor="middle" textLength="560" lengthAdjust="spacingAndGlyphs">BALDETTI COCKTAIL</textPath></text>

  <rect class="flourish" x="440" y="1312" width="340" height="50" rx="25" fill="url(#flourishTone)" role="img" aria-label="Gold scroll flourish divider"/>

  <text class="label-text strength" x="610" y="1415" font-size="58">ABV. 25%</text>
  <text class="label-text volume" x="860" y="1528" font-size="40">70 cl</text>

  <!-- style badge -->
  <rect class="style-badge-frame" x="468" y="1548" width="285" height="114" fill="url(#goldFoil)"/>
  <rect class="style-badge" x="478" y="1558" width="265" height="94" fill="var(--accent-red)"/>
  <text class="display-text style-badge-text" x="610" y="1636" font-size="92" textLength="150" lengthAdjust="spacingAndGlyphs">BITTER</text>
</svg>
</body>
</html>
```